The next stage in our 106 year history in Specialised Stationery

We need a business card design(which is also adaptable for our general stationery) to suit the changing face of our business. Harlow, an Australian company has been the leader in its category since 1907. We design and print various books required by small business to comply with government legislation in regards to keeping records. Accountancy, Payroll, Vehicle usage recording, Firearms registration etc. The Harlow logo a blue diamond is one of the best known in our industry. As manual recording has declined in the last few years we have diversified into other areas: Safety Apparel, Personal Protective Equipment (PPE) and web based software for bookkeeping and Customer Relationship management(CRM). Separate logos have been adopted for each of these being: Harlow Systems, Harlow Safety, Harlow Apparel and Harlow Software each with same diamond but different colour background. This has made it easy to identify the different sectors but difficult to bring together for a Corporate identity in Business cards etc. We are looking to bring all logos together (not one logo) but still allow the logo to depict the diversity of our offering, while still being able to have a category specific logo for each of the divisions. All products go through the same distribution channel, Office Products. The final design should depict an old established company well, known and trusted but leaping forward and still retaining same values they have come to trust.

Target Market(s)

Micro to small business companies generally who employ 20 or less people.

Industry/Entity Type

Small Business

Requirements
Must have
• The diamonds are well recognised and the new design should retain the integrity of them.

```html
<!DOCTYPE html>
<html lang="en">
<head>
<meta charset="utf-8">
<title>Harlow Business Card – Sides A and B</title>
<link rel="stylesheet" href="https://fonts.googleapis.com/css2?family=Open+Sans:wght@700;800&family=Roboto:wght@400;500;700;900&display=swap">
<style>
  :root {
    --board: #8f8f8f;
    --label: #0d0d0d;
    --sky-light: #6ec2ff;
    --sky: #2196f3;
    --sky-deep: #1183ea;
    --navy: #1b3f8f;
    --brand-blue: #1d5fa8;
    --brand-red: #c8102e;
    --brand-orange: #e8582a;
    --brand-green: #2fa83a;
    --paper: #ffffff;
    --rule: #8a8a8a;
    --white: #ffffff;
  }
  * { margin: 0; padding: 0; box-sizing: border-box; }
  html, body { width: 1200px; height: 800px; overflow: hidden; }
  body {
    position: relative;
    background: var(--board);
    font-family: "Roboto", Arial, sans-serif;
  }

  .side-label {
    position: absolute;
    font-family: "Open Sans", Arial, sans-serif;
    font-weight: 800;
    font-size: 50px;
    line-height: 1;
    color: var(--label);
    white-space: nowrap;
    transform: translateX(-50%);
  }
  .label-option-1 { left: 303px; top: 24px; }
  .label-option-2 { left: 888px; top: 24px; }
  .label-side-b  { left: 600px; top: 418px; }

  .card {
    position: absolute;
    width: 524px;
    height: 298px;
    overflow: hidden;
  }
  .card-front {
    top: 100px;
    background: radial-gradient(ellipse 60% 62% at 50% 50%, var(--sky-light) 0%, var(--sky) 65%, var(--sky-deep) 100%);
  }
  .front-option-1 { left: 56px; }
  .front-option-2 { left: 628px; }

  .division-frame { position: absolute; inset: 0; }

  .division-badge {
    position: absolute;
    display: flex;
    align-items: center;
    gap: 6px;
    transform: translate(-50%, -50%);
    white-space: nowrap;
  }
  .badge-square { width: 12px; height: 12px; }
  .badge-name {
    font-weight: 700;
    font-size: 13px;
    color: var(--white);
    letter-spacing: 0.2px;
  }
  .badge-systems  { left: 75px;  top: 48px; }
  .badge-software { left: 451px; top: 48px; }
  .badge-safety   { left: 75px;  top: 250px; }
  .badge-apparel  { left: 451px; top: 250px; }
  .swatch-systems  { background: var(--brand-blue); }
  .swatch-software { background: var(--brand-red); }
  .swatch-safety   { background: var(--brand-orange); }
  .swatch-apparel  { background: var(--brand-green); }

  .front-wordmark {
    position: absolute;
    left: 50%;
    top: 50%;
    transform: translate(-50%, -50%);
    font-weight: 900;
    color: var(--white);
    line-height: 1;
    letter-spacing: 1px;
  }
  .front-option-1 .front-wordmark { font-size: 56px; }
  .front-option-2 .front-wordmark { font-size: 88px; }

  .card-back {
    left: 338px;
    top: 474px;
    height: 300px;
    background: var(--paper);
  }
  .band {
    position: absolute;
    left: 0;
    width: 100%;
    height: 20px;
    display: flex;
  }
  .band span { flex: 1; }
  .band-top { top: 0; }
  .band-bottom { bottom: 0; }
  .band-blue { background: var(--brand-blue); }
  .band-red { background: var(--brand-red); }
  .band-orange { background: var(--brand-orange); }
  .band-green { background: var(--brand-green); }

  .card-divider {
    position: absolute;
    left: 262px;
    top: 40px;
    width: 1.5px;
    height: 219px;
    background: var(--rule);
  }

  .division-list {
    position: absolute;
    left: 36px;
    top: 62px;
    list-style: none;
  }
  .division-list li {
    display: flex;
    align-items: center;
    gap: 8px;
    height: 27px;
  }
  .division-list .badge-square { width: 13px; height: 13px; }
  .division-list .division-name { font-weight: 700; font-size: 15px; }
  .name-systems  { color: var(--brand-blue); }
  .name-software { color: var(--brand-red); }
  .name-safety   { color: var(--brand-orange); }
  .name-apparel  { color: var(--brand-green); }

  .company-name {
    position: absolute;
    left: 27px;
    top: 183px;
    font-weight: 700;
    font-size: 22px;
    color: var(--navy);
  }
  .company-address {
    position: absolute;
    left: 27px;
    top: 211px;
    font-style: normal;
    font-weight: 500;
    font-size: 10.5px;
    line-height: 15px;
    color: var(--brand-red);
  }

  .holder-name {
    position: absolute;
    left: 299px;
    top: 56px;
    font-weight: 700;
    font-size: 22px;
    color: var(--brand-blue);
  }
  .holder-title {
    position: absolute;
    left: 299px;
    top: 88px;
    font-weight: 700;
    font-size: 15px;
    color: var(--brand-red);
  }

  .contact-list {
    position: absolute;
    left: 298px;
    top: 160px;
    list-style: none;
  }
  .contact-list li {
    display: flex;
    align-items: center;
    gap: 7px;
    height: 21px;
    font-weight: 500;
    font-size: 11.5px;
    color: var(--brand-red);
  }
  .contact-icon { width: 13px; height: 13px; flex: none; }
  .contact-icon * { fill: none; stroke: var(--brand-blue); stroke-width: 1.6; stroke-linejoin: round; stroke-linecap: round; }
  .contact-icon .solid { fill: var(--brand-blue); stroke: none; }
</style>
</head>
<body>

  <h2 class="side-label label-option-1">SIDE A: Option 1</h2>
  <h2 class="side-label label-option-2">SIDE A: Option 2</h2>
  <h2 class="side-label label-side-b">SIDE B</h2>

  <!-- Front, option 1: divisions joined by a frame around the parent name -->
  <section class="card card-front front-option-1">
    <svg class="division-frame" width="524" height="298" viewBox="0 0 524 298" aria-hidden="true">
      <g stroke="#ffffff" stroke-width="3" stroke-linecap="square">
        <line x1="150" y1="48" x2="372" y2="48"/>
        <line x1="150" y1="250" x2="372" y2="250"/>
        <line x1="75" y1="66" x2="75" y2="232"/>
        <line x1="451" y1="66" x2="451" y2="232"/>
      </g>
    </svg>
    <div class="division-badge badge-systems"><span class="badge-square swatch-systems"></span><span class="badge-name">Harlow Systems</span></div>
    <div class="division-badge badge-software"><span class="badge-square swatch-software"></span><span class="badge-name">Harlow Software</span></div>
    <div class="division-badge badge-safety"><span class="badge-square swatch-safety"></span><span class="badge-name">Harlow Safety</span></div>
    <div class="division-badge badge-apparel"><span class="badge-square swatch-apparel"></span><span class="badge-name">Harlow Apparel</span></div>
    <p class="front-wordmark">Harlow</p>
  </section>

  <!-- Front, option 2: parent name alone -->
  <section class="card card-front front-option-2">
    <p class="front-wordmark">Harlow</p>
  </section>

  <!-- Back: contact side -->
  <section class="card card-back">
    <div class="band band-top"><span class="band-blue"></span><span class="band-red"></span></div>

    <ul class="division-list">
      <li><span class="badge-square swatch-systems"></span><span class="division-name name-systems">Harlow Systems</span></li>
      <li><span class="badge-square swatch-safety"></span><span class="division-name name-safety">Harlow Safety</span></li>
      <li><span class="badge-square swatch-software"></span><span class="division-name name-software">Harlow Software</span></li>
      <li><span class="badge-square swatch-apparel"></span><span class="division-name name-apparel">Harlow Apparel</span></li>
    </ul>

    <p class="company-name">Harlow Pty Limited</p>
    <address class="company-address">Unit 4, 212 Carrow Street,<br>Bayfield, NSW 2290</address>

    <div class="card-divider"></div>

    <p class="holder-name">YOUR NAME</p>
    <p class="holder-title">Title</p>

    <ul class="contact-list">
      <li>
        <svg class="contact-icon" viewBox="0 0 14 14" aria-hidden="true"><path class="solid" d="M3 1h2.5l1 3-1.6 1.2a7 7 0 0 0 3.9 3.9L10 7.5l3 1V11a2 2 0 0 1-2 2A10 10 0 0 1 1 3a2 2 0 0 1 2-2z"/></svg>
        <span>61 2 9000 3418</span>
      </li>
      <li>
        <svg class="contact-icon" viewBox="0 0 14 14" aria-hidden="true"><rect x="3.5" y="1.5" width="7" height="4"/><rect x="1.5" y="5.5" width="11" height="5" class="solid"/><rect x="3.5" y="9" width="7" height="3.5"/></svg>
        <span>61 2 9000 7265</span>
      </li>
      <li>
        <svg class="contact-icon" viewBox="0 0 14 14" aria-hidden="true"><rect x="1.5" y="3" width="11" height="8" rx="1"/><path d="M1.8 3.5 7 7.8l5.2-4.3"/></svg>
        <span>hello@harlowmail.com.au</span>
      </li>
      <li>
        <svg class="contact-icon" viewBox="0 0 14 14" aria-hidden="true"><circle cx="7" cy="7" r="5.5"/><ellipse cx="7" cy="7" rx="2.3" ry="5.5"/><path d="M1.5 7h11"/></svg>
        <span>www.harlow.com.au</span>
      </li>
    </ul>

    <div class="band band-bottom"><span class="band-orange"></span><span class="band-green"></span></div>
  </section>

</body>
</html>
```